Web Designer criação do designer da loja

preciso que faça o modelo de como seria a loja virtual ( ecommerce ) apenas o desenho da pagina ja possuo o logo e preciso do desenho de como sera a loja virtual e comercializa produtos de informatica e telefonia quero se sigam as regras das cores do logo estou enviando duas logos com os fundo diferentes de preferencia criar o projeto no fundo laranja como consta no logo enviado

Target Market(s)

ecommerce designers

Number of Pages Required

1 page

Font styles to use
Sans Serif

Requirements
Must have
• meu projeto deve-se comparar com as lojas virtuais do momento

```html
<!DOCTYPE html>
<html lang="en">
<head>
<meta charset="utf-8">
<title>Voltra Store</title>
<link rel="stylesheet" href="https://fonts.googleapis.com/css2?family=Open+Sans:wght@300;400;600;700&family=Poiret+One&display=swap">
<style>
:root{
  --orange:#ff5a0a;
  --orange-dark:#b83c05;
  --hero-a:#f38a3e;
  --hero-b:#e4541c;
  --yellow:#f7c21e;
  --page:#e4e4e4;
  --topbar:#f1f1f1;
  --ink:#333;
  --muted:#666;
  --white:#fff;
  --black:#151515;
}
*{box-sizing:border-box;margin:0;padding:0}
html,body{width:700px;height:1200px;overflow:hidden}
body{font-family:"Open Sans",Arial,sans-serif;color:var(--ink);background:var(--page);position:relative}
.abs{position:absolute}
.topbar{left:0;top:0;width:700px;height:24px;background:var(--topbar);font-size:7px;color:var(--muted)}
.topbar span{position:absolute;top:7px}
.topbar .accent{color:var(--orange)}
.header{left:0;top:24px;width:700px;height:64px;background:var(--white)}
.logo{font-weight:700;color:var(--orange);font-size:20px;letter-spacing:-.3px;display:flex;align-items:center;gap:6px}
.logo i{display:block;width:9px;height:9px;background:var(--orange)}
.phone{left:308px;top:30px;font-size:7px;color:var(--ink);display:flex;align-items:center;gap:5px}
.search{left:420px;top:24px;width:114px;height:15px;border:1px solid #ddd;border-radius:8px}
.currency{left:426px;top:44px;font-size:7px;color:#aaa}
.currency b{color:var(--orange);font-weight:400}
.flag{left:482px;top:45px;width:10px;height:7px;background:linear-gradient(#c33 0 50%,#fff 50%);border-left:4px solid #236}
.basket{left:550px;top:26px;font-size:8px;display:flex;align-items:center;gap:5px}
.nav{left:0;top:88px;width:700px;height:26px;background:linear-gradient(#f4f4f4,#cfcfcf);font-size:8px}
.nav a{position:absolute;top:0;height:26px;line-height:26px;color:var(--ink);text-decoration:none;padding:0 10px;border-right:1px solid #bbb}
.nav a.active{background:var(--orange-dark);color:var(--white);border:0}
.nav .pointer{left:117px;top:114px;width:0;height:0;border-left:6px solid transparent;border-right:6px solid transparent;border-top:7px solid var(--orange-dark);z-index:2}
.hero{left:0;top:114px;width:700px;height:300px;background:radial-gradient(ellipse at 40% 45%,var(--hero-a),var(--hero-b) 75%)}
.hero .kicker{left:137px;top:66px;width:200px;text-align:center;font-family:"Poiret One",sans-serif;font-size:16px;color:#3a1a08}
.hero h1{left:110px;top:90px;width:255px;text-align:center;font-family:"Poiret One",sans-serif;font-weight:400;font-size:27px;color:var(--white)}
.hero .sub{left:137px;top:118px;width:200px;text-align:center;font-weight:300;font-size:12px;color:var(--white)}
.hero .cta{left:209px;top:143px;width:64px;height:64px;border-radius:50%;background:var(--yellow);box-shadow:0 0 0 3px rgba(255,220,80,.4);font-size:8px;color:#6a3a00;text-align:center;line-height:64px}
.hero .devices{left:365px;top:45px;width:200px;height:205px;border-radius:6px;background:linear-gradient(140deg,#2a2a2a,#5b5b5b 55%,#1b1b1b)}
.hero .arrow{top:140px;width:20px;height:20px;border-radius:50%;background:rgba(170,70,20,.55)}
.hero .dot{top:274px;width:8px;height:8px;border-radius:50%;border:1px solid var(--white)}
.tile{border:2px solid var(--white)}
.photo-phone{left:100px;top:445px;width:340px;height:136px;background:linear-gradient(120deg,#a7c4ad,#d7e3cf 45%,#7fa88f)}
.overlay{background:var(--white);text-align:center;font-size:8px;line-height:13px;color:var(--ink);display:flex;align-items:center;justify-content:center}
.about{left:458px;top:445px;width:141px;height:136px;background:var(--orange);color:var(--white);padding:9px 14px}
.about h2{font-weight:400;font-size:11px}
.about .tag{font-size:7px;margin-top:6px;color:#ffe0cc}
.about p{font-size:6px;line-height:9px;margin-top:4px}
.about .btn{position:absolute;left:72px;top:111px;width:50px;height:13px;border:1px solid var(--white);font-size:6px;text-align:center;line-height:11px}
.subscribe{left:100px;top:599px;width:98px;height:138px;background:var(--black);color:var(--white);padding:6px 8px}
.subscribe h2{font-weight:400;font-size:11px}
.subscribe p{font-size:6px;line-height:9px;margin-top:6px}
.subscribe .field{position:absolute;left:8px;top:82px;width:80px;height:15px;background:var(--white);color:#777;font-size:6px;line-height:15px;text-align:center}
.subscribe .send{position:absolute;left:8px;top:104px;width:80px;height:15px;background:var(--orange);font-size:6px;line-height:15px;text-align:center}
.offer{left:215px;top:599px;width:98px;height:138px;background:var(--white)}
.offer .pic{position:absolute;left:0;top:0;width:94px;height:81px;background:linear-gradient(160deg,#3d4b63,#9fb3c9 50%,#2b3346)}
.offer .t1{position:absolute;top:92px;width:94px;text-align:center;font-size:11px}
.offer .t2{position:absolute;top:110px;width:94px;text-align:center;font-size:8px}
.photo-beach{left:330px;top:599px;width:269px;height:138px;background:linear-gradient(#bcd8e4,#e8ddc4 55%,#5d8fa2 70%,#9ab8c2)}
.section-title{left:150px;top:776px;width:400px;text-align:center;font-size:16px;color:var(--ink)}
.section-sub{left:150px;top:797px;width:400px;text-align:center;font-size:7px;color:var(--muted)}
.sq{top:787px;width:16px;height:16px;display:flex;align-items:center;justify-content:center}
.rule{left:100px;top:816px;width:500px;border-top:1px dashed #bbb}
.card{top:831px;width:120px;height:153px;background:var(--white)}
.card .pic{position:absolute;left:25px;top:10px;width:70px;height:100px;border-radius:6px;background:linear-gradient(150deg,#222,#666 60%,#333)}
.price{width:54px;height:16px;background:var(--orange);color:var(--white);font-size:7px;text-align:center;line-height:16px}
.card .price{position:absolute;left:13px;top:124px}
.namebar{left:103px;top:946px;width:114px;height:15px;background:#e3e3e3;font-size:7px;text-align:center;line-height:15px}
.iconbtn{top:965px;width:36px;height:16px;background:#dadada;display:flex;align-items:center;justify-content:center}
.footer{left:0;top:1043px;width:700px;height:130px;background:var(--white)}
.notch{left:345px;top:1031px;width:0;height:0;border-left:10px solid transparent;border-right:10px solid transparent;border-bottom:12px solid var(--white)}
.social{top:1114px;width:16px;height:16px;border-radius:50%;border:1px solid #888}
.col h3{font-weight:400;font-size:10px;color:var(--ink);margin-bottom:8px}
.col li{list-style:none;font-size:6px;color:#555;margin-bottom:5px}
.col li::before{content:">";margin-right:6px;color:#888}
.col li.on{color:var(--orange)}
.bottombar{left:0;top:1173px;width:700px;height:27px;background:var(--orange);color:var(--white);font-size:6px}
.card-badge{top:1183px;width:14px;height:9px;border-radius:1px;background:var(--white)}
</style>
</head>
<body>

<div class="abs topbar">
  <span class="accent" style="left:100px">Login</span>
  <span style="left:128px;color:#aaa">|</span>
  <span style="left:140px">Create an Account</span>
  <span class="accent" style="left:401px">Wish List (0)</span>
  <span style="left:446px">|</span>
  <span style="left:456px">My Account</span>
  <span style="left:498px">|</span>
  <span style="left:507px">Shopping Cart</span>
  <span style="left:557px">|</span>
  <span style="left:567px">Checkout</span>
</div>

<div class="abs header">
  <div class="abs logo" style="left:100px;top:16px"><i></i>Voltra Store</div>
  <div class="abs phone">
    <svg width="9" height="11" viewBox="0 0 9 11"><path d="M2 0 L4 3 L3 4 Q4 7 6 8 L7 7 L9 9 L7 11 Q0 8 0 2 Z" fill="#444"/></svg>
    Tel: (+00) 555.010.2030
  </div>
  <div class="abs search">
    <svg class="abs" style="right:5px;top:3px" width="9" height="9" viewBox="0 0 9 9"><circle cx="4" cy="4" r="3" fill="none" stroke="#aaa"/><path d="M6 6 L8.5 8.5" stroke="#aaa"/></svg>
  </div>
  <div class="abs currency"><b>$</b> | € | £</div>
  <div class="abs flag"></div>
  <div class="abs basket">
    <svg width="14" height="12" viewBox="0 0 14 12"><path d="M0 1 H3 L5 8 H12 L13 3 H4" fill="none" stroke="#ff5a0a" stroke-width="1.4"/><circle cx="6" cy="10.5" r="1.2" fill="#ff5a0a"/><circle cx="11" cy="10.5" r="1.2" fill="#ff5a0a"/></svg>
    Basket (0)
  </div>
</div>

<nav class="abs nav">
  <a class="active" style="left:98px;padding:0 13px">Home</a>
  <a style="left:155px">Electronics</a>
  <a style="left:225px">Parts &amp; Accessories</a>
  <a style="left:326px">Components</a>
  <a style="left:404px">Gallery</a>
  <a style="left:460px">Blog</a>
  <a style="left:507px;border:0">TelephonyMobiles</a>
</nav>
<div class="abs pointer nav" style="background:none;height:0;width:0;left:117px;top:114px;border-left:6px solid transparent;border-right:6px solid transparent;border-top:7px solid var(--orange-dark)"></div>

<section class="abs hero">
  <div class="abs kicker">LOREM IPSUM</div>
  <h1 class="abs">New collections</h1>
  <div class="abs sub">for Mobiles</div>
  <div class="abs cta">VIEW</div>
  <div class="abs devices" role="img" aria-label="Group of smartphones and a tablet with a discount tag"></div>
  <div class="abs arrow" style="left:80px"><svg width="20" height="20"><path d="M12 6 L7 10 L12 14Z" fill="#fff"/></svg></div>
  <div class="abs arrow" style="left:601px"><svg width="20" height="20"><path d="M8 6 L13 10 L8 14Z" fill="#fff"/></svg></div>
  <div class="abs dot" style="left:329px;background:var(--orange);border-color:#ffb08a"></div>
  <div class="abs dot" style="left:341px"></div>
  <div class="abs dot" style="left:353px"></div>
</section>

<div class="abs tile photo-phone" role="img" aria-label="Vintage rotary telephone against a green textured wall">
  <div class="abs overlay" style="left:127px;top:34px;width:68px;height:68px">SHOP<br>Lorem ipsum<br>at 30% off</div>
</div>

<div class="abs tile about">
  <h2>About Us</h2>
  <div class="tag">best online store</div>
  <p>Our theme is one of the best smooth, modern, tremendous templates with a flexible design, high quality and plenty of options for running any type of online shop.</p>
  <div class="btn">VIEW</div>
</div>

<div class="abs tile subscribe">
  <h2>Subscribe</h2>
  <p>Subscribe for our monthly newsletter. to get offer and new collection of cloths, its free and awesome</p>
  <div class="field">Enter you email id</div>
  <div class="send">Subscribe</div>
</div>

<div class="abs tile offer">
  <div class="pic" role="img" aria-label="Smartphone standing on a reflective blue surface"></div>
  <div class="t1">SHOP</div>
  <div class="t2">25% offer on Lorems</div>
</div>

<div class="abs tile photo-beach" role="img" aria-label="Man on the phone giving a thumbs up by the sea">
  <div class="abs overlay" style="left:85px;top:34px;width:68px;height:68px">SHOP<br>Contantry pop<br>at 30% off</div>
</div>

<div class="abs section-title">Our New Products</div>
<div class="abs section-sub">New products for our best customer like you</div>
<div class="abs sq" style="left:100px;background:var(--orange)"><svg width="8" height="10"><path d="M6 1 L2 5 L6 9" fill="none" stroke="#fff" stroke-width="2"/></svg></div>
<div class="abs sq" style="left:585px;background:#888"><svg width="8" height="10"><path d="M2 1 L6 5 L2 9" fill="none" stroke="#fff" stroke-width="2"/></svg></div>
<div class="abs rule"></div>

<div class="abs card" style="left:100px">
  <div class="pic" role="img" aria-label="Black touchscreen mobile phone"></div>
  <svg class="abs" style="left:106px;top:8px" width="10" height="10" viewBox="0 0 10 10"><path d="M8 5 A3 3 0 1 1 6.5 2.4" fill="none" stroke="#777" stroke-width="1.2"/><path d="M5.5 0.8 L8 2 L6 4" fill="none" stroke="#777" stroke-width="1.2"/></svg>
</div>
<div class="abs namebar">Lorem ipsum dolor</div>
<div class="abs iconbtn" style="left:103px"><svg width="10" height="9"><path d="M5 9 L1 5 A2.3 2.3 0 0 1 5 2 A2.3 2.3 0 0 1 9 5Z" fill="#777"/></svg></div>
<div class="abs iconbtn" style="left:142px"><svg width="10" height="10"><path d="M3 7 L7 3" stroke="#777" stroke-width="1.4"/><rect x="1" y="5" width="4" height="4" rx="2" fill="none" stroke="#777"/><rect x="5" y="1" width="4" height="4" rx="2" fill="none" stroke="#777"/></svg></div>
<div class="abs iconbtn" style="left:181px;background:var(--orange)"><svg width="13" height="11"><path d="M0 1 H3 L5 7 H11 L12 3 H4" fill="none" stroke="#fff" stroke-width="1.3"/><circle cx="6" cy="9.5" r="1" fill="#fff"/><circle cx="10" cy="9.5" r="1" fill="#fff"/></svg></div>
<div class="abs price" style="left:100px;top:985px">$394.48</div>

<div class="abs card" style="left:227px">
  <div class="pic" style="left:20px;top:25px;width:80px;height:65px" role="img" aria-label="Office desk phone with display"></div>
  <div class="price">$394.48</div>
</div>
<div class="abs card" style="left:353px">
  <div class="pic" style="left:38px;top:25px;width:44px;height:70px" role="img" aria-label="Black candybar mobile phone"></div>
  <div class="price">$394.48</div>
</div>
<div class="abs card" style="left:480px">
  <div class="pic" style="left:30px;top:22px;width:60px;height:75px;background:linear-gradient(150deg,#3a3a3a,#8a8a8a 50%,#2a2a2a)" role="img" aria-label="Network interface expansion card"></div>
  <div class="price">$394.48</div>
</div>

<div class="abs notch"></div>
<footer class="abs footer">
  <div class="abs logo" style="left:102px;top:23px;font-size:17px"><i></i>Voltra Store</div>
  <div class="abs social" style="left:117px;top:71px"></div>
  <div class="abs social" style="left:137px;top:71px"></div>
  <div class="abs social" style="left:157px;top:71px"></div>
  <div class="abs social" style="left:177px;top:71px"></div>

  <div class="abs col" style="left:274px;top:25px">
    <h3>Information</h3>
    <ul><li class="on">About Us</li><li>Delivery Information</li><li>Privacy Policy</li><li>Terms &amp; Conditions</li></ul>
  </div>
  <div class="abs col" style="left:376px;top:25px">
    <h3>Service</h3>
    <ul><li>Contact Us</li><li>Returns</li><li>Site Map</li></ul>
  </div>
  <div class="abs col" style="left:461px;top:25px">
    <h3>Extras</h3>
    <ul><li>Brands</li><li>Gift Vouchers</li><li>Affiliates</li><li>Specials</li></ul>
  </div>
  <div class="abs col" style="left:548px;top:25px">
    <h3>My account</h3>
    <ul><li>My Account</li><li>Order History</li><li>Wish List</li><li>Newsletter</li></ul>
  </div>
</footer>

<div class="abs bottombar">
  <span class="abs" style="left:100px;top:10px">Copyright © 2015 yoursite, All Right Reserved</span>
  <span class="abs" style="left:485px;top:10px">We Accept :</span>
</div>
<div class="abs card-badge" style="left:527px"></div>
<div class="abs card-badge" style="left:546px"></div>
<div class="abs card-badge" style="left:565px"></div>
<div class="abs card-badge" style="left:584px"></div>

</body>
</html>
```